2026 Marwick Dust Control Municipal Advertisement

I need a professional print advertisement designed for our road dust control business for a 2026 municipal/public works publication.

Our company manufactures, supplies, delivers and applies liquid road dust suppressant products to municipalities, contractors and commercial customers across Ontario.

I will upload:

* Our new truck/application photo to use as the main image
* Our advertisement from last year as a reference for the general style and information

I would like the new advertisement to look modern, professional, industrial and appropriate for municipal/public works decision-makers. The truck photo should be the main visual.

Please include the following wording:

MARWICK DUST CONTROL PRODUCTS
418307 Ontario Limited
Based in Clinton, Ontario

ROAD DUST CONTROL PRODUCTS

Manufacturer & Distributor of Liquid Road Dust Suppressants

AVAILABLE CONCENTRATIONS

35%
Liquid Calcium Magnesium Chloride Solution

30%

20%

Bulk Supply • Delivery • Road Application

Supplying Municipalities, Contractors & Commercial Customers Across Ontario

519-555-0187
dermarw417@quillpost.net

Please make “ROAD DUST CONTROL PRODUCTS” one of the most prominent pieces of wording.

The 35%, 30% and 20% product concentrations should also be large, clear and easy to read.

“MARWICK DUST CONTROL PRODUCTS” should be prominently branded, with “418307 Ontario Limited” smaller underneath.

Please do not overcrowd the advertisement. It should be easy for someone flipping through a municipal publication to understand within a few seconds what we sell and how to contact us.

```html
<!DOCTYPE html>
<html lang="en">
<head>
<meta charset="utf-8">
<title>Marwick Dust Control Products – 2026 Municipal Advertisement</title>
<link href="https://fonts.googleapis.com/css2?family=Rubik:ital,wght@0,400;0,500;0,600;0,700;0,800;1,500&family=Oswald:wght@400;600;700&family=Barlow+Semi+Condensed:wght@600;700;800&display=swap" rel="stylesheet">
<style>
  :root {
    --backdrop: #6a6a6a;
    --navy-deep: #0f1838;
    --navy: #17234f;
    --navy-band: #27346f;
    --panel-black: #0b0d14;
    --yellow: #f6c230;
    --white: #ffffff;
    --silver-top: #ffffff;
    --silver-bottom: #9a9ca3;
    --road-tan: #a88f76;
    --grass: #4d6a3a;
  }
  * { box-sizing: border-box; margin: 0; padding: 0; }
  html, body { width: 1027px; height: 1200px; overflow: hidden; }
  body { background: var(--backdrop); font-family: "Rubik", sans-serif; position: relative; }

  .ad {
    position: absolute; left: 103px; top: 85px; width: 802px; height: 1037px;
    background: linear-gradient(180deg, var(--navy-deep) 0%, var(--navy) 55%, var(--navy-deep) 100%);
    overflow: hidden; color: var(--white);
  }

  .hero-photo {
    position: absolute; left: 418px; top: 0; width: 384px; height: 560px;
    background:
      linear-gradient(180deg, rgba(15,24,56,0) 70%, var(--navy-deep) 100%),
      linear-gradient(90deg, var(--navy-deep) 0%, rgba(15,24,56,0) 30%),
      linear-gradient(90deg, var(--grass) 0%, var(--road-tan) 18%, #b59c82 50%, var(--road-tan) 82%, var(--grass) 100%);
  }

  .title-art { position: absolute; left: 0; top: 0; width: 802px; height: 560px; }
  .title-art text { font-family: "Barlow Semi Condensed", sans-serif; }
  .title-art .brand-name { font-weight: 700; font-size: 78px; fill: var(--white); }
  .title-art .brand-sub { font-weight: 600; font-size: 30px; fill: var(--white); }
  .title-art .brand-reg { font-family: "Rubik", sans-serif; font-weight: 400; font-size: 15px; fill: var(--yellow); }
  .title-art .road { font-weight: 800; font-size: 171px; fill: var(--white); }
  .title-art .dust { font-weight: 800; font-size: 63px; fill: var(--white); }
  .title-art .products { font-weight: 800; font-size: 83px; fill: var(--yellow); }
  .title-art .based { font-weight: 700; font-size: 21px; fill: var(--white); }
  .title-art .city { font-weight: 700; font-size: 31px; fill: var(--white); }

  .tagline { position: absolute; left: 45px; top: 458px; width: 422px; height: 68px; }
  .tagline svg { position: absolute; inset: 0; }
  .tagline p { position: relative; padding: 8px 0 0 20px; font-weight: 500; font-size: 18.5px; line-height: 26px; white-space: nowrap; }

  .map-area { position: absolute; left: 678px; top: 326px; width: 73px; height: 67px; background: rgba(255,255,255,0.18); border-radius: 4px; }

  .conc-title { position: absolute; left: 0; top: 572px; width: 802px; text-align: center; font-weight: 600; font-size: 25px; letter-spacing: 1px; }

  .conc-panels { position: absolute; left: 0; top: 614px; width: 802px; height: 190px; }
  .conc { position: absolute; top: 614px; width: 200px; text-align: center; font-family: "Oswald", sans-serif; }
  .conc .value { font-weight: 700; font-size: 96px; line-height: 100px; margin-top: 6px; white-space: nowrap;
    background: linear-gradient(180deg, var(--silver-top) 30%, var(--silver-bottom) 100%);
    -webkit-background-clip: text; background-clip: text; color: transparent; }
  .conc .value sup { font-size: 42px; vertical-align: top; line-height: 60px; margin-left: 2px; }
  .conc .desc { font-weight: 400; font-size: 20px; line-height: 24px; color: var(--white); }

  .services { position: absolute; left: 0; top: 831px; width: 802px; height: 83px; background: var(--white); }
  .service { position: absolute; top: 0; height: 83px; display: flex; align-items: center; gap: 10px; color: var(--navy); font-weight: 600; font-size: 23px; white-space: nowrap; }
  .service .icon { width: 52px; height: 52px; flex: none; }

  .audience { position: absolute; left: 0; top: 914px; width: 802px; height: 46px; background: var(--yellow); color: var(--navy-deep); text-align: center; font-style: italic; font-weight: 500; font-size: 18.5px; line-height: 46px; white-space: nowrap; }

  .contact { position: absolute; left: 0; top: 960px; width: 802px; height: 77px; }
  .contact-item { position: absolute; top: 13px; display: flex; align-items: center; gap: 10px; font-weight: 600; font-size: 22px; white-space: nowrap; }
  .contact-item svg { width: 52px; height: 52px; flex: none; }
</style>
</head>
<body>
<main class="ad">
  <div class="hero-photo" role="img" aria-label="Aerial photo of a blue tanker truck applying liquid dust suppressant on a gravel road"></div>

  <svg class="title-art" viewBox="0 0 802 560" role="img" aria-label="Marwick Dust Control Products, Ontario Limited 418307. Road Dust Control Products. Based in Clinton, Ontario">
    <text class="brand-name" x="45" y="94" textLength="309" lengthAdjust="spacingAndGlyphs">MARWICK</text>
    <rect x="45" y="104" width="306" height="2" fill="var(--yellow)"/>
    <text class="brand-sub" x="46" y="136" textLength="308" lengthAdjust="spacingAndGlyphs">DUST CONTROL PRODUCTS</text>
    <text class="brand-reg" x="108" y="158" textLength="167" lengthAdjust="spacingAndGlyphs">Ontario Limited 418307</text>

    <text class="road" x="45" y="313" textLength="366" lengthAdjust="spacingAndGlyphs">ROAD</text>
    <text class="dust" x="45" y="367" textLength="366" lengthAdjust="spacingAndGlyphs">DUST CONTROL</text>
    <text class="products" x="45" y="439" textLength="366" lengthAdjust="spacingAndGlyphs">PRODUCTS</text>

    <text class="based" x="679" y="416" textLength="75" lengthAdjust="spacingAndGlyphs">BASED IN</text>
    <text class="city" x="679" y="444" textLength="100" lengthAdjust="spacingAndGlyphs">CLINTON</text>
    <text class="city" x="679" y="470" textLength="102" lengthAdjust="spacingAndGlyphs">ONTARIO</text>
    <rect x="680" y="480" width="100" height="1.5" fill="var(--white)"/>
    <rect x="680" y="484" width="58" height="1.5" fill="var(--white)"/>
    <rect x="680" y="488" width="58" height="1.5" fill="var(--white)"/>
  </svg>

  <div class="map-area" role="img" aria-label="Outline map of Canada"></div>

  <div class="tagline">
    <svg viewBox="0 0 422 68" width="422" height="68" aria-hidden="true">
      <polygon points="0,0 392,0 360,68 0,68" fill="var(--navy-band)"/>
      <polygon points="402,0 412,0 380,68 370,68" fill="var(--yellow)"/>
    </svg>
    <p>Manufacturer &amp; Distributor of Liquid<br>Road Dust Suppressants</p>
  </div>

  <h2 class="conc-title">AVAILABLE CONCENTRATIONS</h2>

  <svg class="conc-panels" viewBox="0 0 802 190" aria-hidden="true">
    <polygon points="83,0 301,0 257,189 39,189" fill="var(--panel-black)" stroke="var(--yellow)" stroke-width="1"/>
    <polygon points="315,0 534,0 490,189 272,189" fill="var(--panel-black)" stroke="var(--yellow)" stroke-width="1"/>
    <polygon points="548,0 768,0 724,189 505,189" fill="var(--panel-black)" stroke="var(--yellow)" stroke-width="1"/>
  </svg>

  <section class="conc" style="left:69px">
    <div class="value">35<sup>%</sup></div>
    <p class="desc">Liquid Calcium<br>Magnesium Chloride<br>Solution</p>
  </section>
  <section class="conc" style="left:302px">
    <div class="value">30<sup>%</sup></div>
    <p class="desc">Liquid Calcium<br>Magnesium Chloride<br>Solution</p>
  </section>
  <section class="conc" style="left:535px">
    <div class="value">20<sup>%</sup></div>
    <p class="desc">Liquid Calcium<br>Magnesium Chloride<br>Solution</p>
  </section>

  <div class="services">
    <div class="service" style="left:54px">
      <svg class="icon" viewBox="0 0 52 52" aria-hidden="true">
        <circle cx="26" cy="26" r="26" fill="var(--navy)"/>
        <g fill="none" stroke="#fff" stroke-width="1.4">
          <rect x="15" y="14" width="10" height="24"/><rect x="25" y="26" width="12" height="12"/><line x1="15" y1="22" x2="25" y2="22"/><line x1="15" y1="30" x2="25" y2="30"/>
        </g>
      </svg>
      <span>BULK SUPPLY</span>
    </div>
    <div class="service" style="left:302px">
      <svg class="icon" viewBox="0 0 52 52" aria-hidden="true">
        <circle cx="26" cy="26" r="26" fill="var(--navy)"/>
        <g fill="none" stroke="#fff" stroke-width="1.4">
          <rect x="12" y="20" width="18" height="13"/><path d="M30 24h6l4 5v4H30z"/><circle cx="18" cy="35" r="3"/><circle cx="34" cy="35" r="3"/><rect x="17" y="13" width="8" height="7"/>
        </g>
      </svg>
      <span>DELIVERY</span>
    </div>
    <div class="service" style="left:489px">
      <svg class="icon" viewBox="0 0 52 52" aria-hidden="true">
        <circle cx="26" cy="26" r="26" fill="var(--navy)"/>
        <g fill="none" stroke="#fff" stroke-width="1.4">
          <path d="M18 40V24q0-8 8-8h8"/><path d="M24 40V26q0-4 4-4h6"/><path d="M21 38v-3M21 31v-3" stroke-dasharray="2 2"/><circle cx="37" cy="15" r="3"/>
        </g>
      </svg>
      <span>ROAD APPLICATION</span>
    </div>
  </div>

  <div class="audience">Supplying Municipalities, Contractors &amp; Commercial Customers Across Ontario</div>

  <footer class="contact">
    <div class="contact-item" style="left:124px">
      <svg viewBox="0 0 52 52" aria-hidden="true">
        <circle cx="26" cy="26" r="24.5" fill="none" stroke="var(--yellow)" stroke-width="1.5"/>
        <path d="M19 15l4 0 2 6-3 2q2 5 7 7l2-3 6 2v4q-1 3-4 3q-17-2-18-18q0-3 4-3z" fill="none" stroke="#fff" stroke-width="1.4"/>
      </svg>
      <span>519-555-0187</span>
    </div>
    <div class="contact-item" style="left:359px">
      <svg viewBox="0 0 52 52" aria-hidden="true">
        <circle cx="26" cy="26" r="24.5" fill="none" stroke="var(--yellow)" stroke-width="1.5"/>
        <g fill="none" stroke="#fff" stroke-width="1.4"><rect x="14" y="18" width="24" height="16"/><path d="M14 18l12 10 12-10M14 34l9-8M38 34l-9-8"/></g>
      </svg>
      <span>dermarw417@quillpost.net</span>
    </div>
  </footer>
</main>
</body>
</html>
```